Bref créative
BRN Tek
B-cards, letter head and envelopes
I need single sided standard sized Business Card [3.5" x 2"]
use same font or others...other fonts are welcome
Simple
Gareth Pembly
CEO
482 Harlowe Street, Suite 1730
San Francisco, California 94111
gpembly@brnqel.com
brnqel.com
-use this logo in the business cards, letterhead and envelopes.
-we are looking for designs with and with out a water mark using parts or the entire logo.

```html
<!DOCTYPE html>
<html lang="en">
<head>
<meta charset="utf-8">
<title>BRN Tek — Business Card</title>
<link href="https://fonts.googleapis.com/css2?family=Arimo:wght@400;700&display=swap" rel="stylesheet">
<style>
  :root {
    --green: #8cc63e;
    --blue: #2f5f8a;
    --ink: #111111;
    --grey: #555a5f;
    --paper: #ffffff;
    --edge: #c9c9c9;
  }
  html, body { margin: 0; padding: 0; overflow: hidden; background: var(--paper); }
  .card {
    position: relative;
    width: 1200px; height: 686px;
    box-sizing: border-box;
    border: 2px solid var(--edge);
    background: var(--paper);
    font-family: "Arimo", Arial, sans-serif;
    color: var(--ink);
    overflow: hidden;
  }
  .brand-name {
    position: absolute; left: 60px; top: 150px;
    margin: 0;
    font-size: 72px; font-weight: 700; line-height: 1;
    color: var(--ink);
  }
  .tagline {
    position: absolute; left: 60px; top: 296px;
    font-size: 27px; color: var(--grey);
  }
  .divider { position: absolute; left: 591px; width: 5px; }
  .divider--blue { top: 44px; height: 304px; background: var(--blue); }
  .divider--green { top: 348px; height: 300px; background: var(--green); }
  .person { position: absolute; right: 40px; top: 30px; text-align: right; }
  .person-name { font-size: 35px; font-weight: 700; margin: 0; }
  .person-title { font-size: 30px; margin: 12px 0 0; }
  .phones {
    position: absolute; right: 40px; top: 364px;
    text-align: right; font-size: 32px; line-height: 38px;
  }
  .label { color: var(--green); font-weight: 700; }
  .online {
    position: absolute; left: 42px; top: 570px;
    font-size: 32px; line-height: 42px;
  }
  .address {
    position: absolute; left: 680px; top: 570px;
    font-size: 32px; line-height: 42px;
  }
</style>
</head>
<body>
  <div class="card">
    <p class="brand-name">BRN Tek</p>
    <div class="tagline">Bright Relay Networks</div>

    <div class="divider divider--blue"></div>
    <div class="divider divider--green"></div>

    <div class="person">
      <p class="person-name">Gareth Pembly</p>
      <p class="person-title">CEO</p>
    </div>

    <div class="phones">
      <div><span class="label">T:</span> 800-555-0148</div>
      <div><span class="label">P:</span> 414-555-0172</div>
      <div><span class="label">C:</span> 415-555-0193</div>
      <div><span class="label">F:</span> 415-555-0126</div>
    </div>

    <div class="online">
      <div><span class="label">E :</span> gpembly@brnqel.com</div>
      <div><span class="label">W:</span> www.brnqel.com</div>
    </div>

    <div class="address">
      <div>482 Harlowe Street, Suite 1730</div>
      <div>San Francisco, California 94111</div>
    </div>
  </div>
</body>
</html>
```